Design & Build a WordPress Website for “Quietfern Meditation” (Australian Charity Rebrand)

We are a registered Australian charity currently known as Tavolin Meditation Australia.

We are rebranding our public identity to “Quietfern Meditation” to make the meditation practice easier to understand and more relatable for people in Australia and New Zealand.

We are looking for an experienced WordPress designer + developer to design and build a complete website that reflects:

Peace

Trust

Authentic Himalayan roots

Simplicity

Spiritual depth without being religious

Warmth, friendliness, and community feeling

This is not a corporate website. This is a meditation movement website for a non-profit organisation.

Target Market(s)

Australia and New Zealand - Age 25-65

Industry/Entity Type

Not of profit meditation organisation

Requirements
Must have
• Included in the design brief attached
Nice to have
Should not have

```html
<!DOCTYPE html>
<html lang="en">
<head>
<meta charset="utf-8">
<title>Quietfern Meditation</title>
<link rel="stylesheet" href="https://fonts.googleapis.com/css2?family=Bebas+Neue&family=Montserrat:wght@400;500;600;700&display=swap">
<style>
:root{
  --purple:#a784c8;
  --purple-dark:#9a74bf;
  --coral:#e9867c;
  --ink:#2a2a2a;
  --muted:#555;
  --lavender:#f6eafc;
  --blush:#fdeeeb;
  --footer:#1b1515;
  --white:#fff;
}
*{box-sizing:border-box;margin:0;padding:0}
html,body{width:1200px;height:3567px;overflow:hidden}
body{font-family:"Montserrat",sans-serif;color:var(--ink);background:var(--white);position:relative}
.abs{position:absolute}
.heading{font-family:"Bebas Neue",sans-serif;color:var(--purple);font-weight:400;letter-spacing:.5px;text-align:center}
.btn{position:absolute;display:flex;align-items:center;justify-content:center;background:var(--purple);color:#fff;border-radius:20px;font-size:11px;font-weight:600;letter-spacing:.3px;text-transform:uppercase}
.round{position:absolute;width:31px;height:31px;border-radius:50%;background:var(--purple);display:flex;align-items:center;justify-content:center}
.mark{position:absolute;left:588px;width:24px;height:24px;border-radius:50%;border:2px solid var(--coral)}
.photo{position:absolute}

/* hero */
.hero{position:absolute;left:0;top:0;width:1200px;height:644px;background:radial-gradient(ellipse at 50% 45%,#8a4a22 0%,#4a2e1d 40%,#241a14 80%)}
.logo{position:absolute;display:flex;align-items:center;gap:10px}
.logo-dot{width:44px;height:44px;border-radius:50%;background:var(--coral)}
.logo-name{color:var(--coral);font-weight:700;font-size:15px;line-height:1.15;text-transform:uppercase;letter-spacing:.5px}
.nav{position:absolute;left:305px;top:32px;display:flex;gap:26px;font-size:12px;color:#fff}
.nav .active{color:var(--coral);text-decoration:underline}
.nav .region{color:var(--purple);text-decoration:underline;font-weight:600}
.hero-title{position:absolute;left:0;width:1200px;text-align:center;font-family:"Bebas Neue",sans-serif}
.hero-title .l1{display:block;color:#fff;font-size:37px;line-height:1}
.hero-title .l2{display:block;font-size:68px;line-height:1;margin-top:4px;color:var(--coral)}
.hero-title .l2 b{color:#fff;font-weight:400}

/* about */
.intro{position:absolute;left:300px;width:600px;top:798px;text-align:center;font-size:11.5px;line-height:1.35}
.feature{position:absolute;width:220px;text-align:center;font-size:12.5px;line-height:1.25}
.feature svg{display:block;margin:0 auto 8px}
.org-text{position:absolute;left:656px;width:385px;font-size:11px;line-height:1.37}

/* sessions */
.sessions{position:absolute;left:0;top:1446px;width:1200px;height:613px;background:var(--lavender)}
.card{position:absolute;top:166px;width:204px;height:306px;background:#fff;border-radius:3px}
.card .img{height:131px;border-radius:3px 3px 0 0}
.card h3{font-size:13.5px;color:var(--coral);font-weight:700;margin:16px 14px 6px;line-height:1.15}
.row{display:flex;gap:6px;font-size:10px;line-height:1.5;margin:0 14px 6px;color:var(--muted)}
.row svg{flex:none;margin-top:2px}
.row u{color:var(--ink)}

/* events */
.ev-title{font-size:14px;color:var(--coral);font-weight:600;line-height:1.25}
.ev-meta{display:flex;gap:6px;align-items:center;font-size:10px;color:var(--muted);margin-top:8px}
.divider{position:absolute;height:1px;background:#eee}

/* resources */
.resources{position:absolute;left:0;top:2664px;width:1200px;height:630px;background:var(--blush)}
.tag{position:absolute;top:10px;left:10px;background:#222;color:#fff;font-size:10px;padding:2px 8px;border-radius:2px}
.res-cap{position:absolute;display:flex;gap:14px;align-items:center;font-size:12.5px;font-weight:600;line-height:1.25}

/* footer */
.footer{position:absolute;left:0;top:3294px;width:1200px;height:233px;background:var(--footer);color:#ddd}
.footer h4{color:var(--coral);font-size:13px;font-weight:700;margin-bottom:10px}
.fcol{position:absolute;top:54px;font-size:11px;line-height:1.6}
.social{position:absolute;top:158px;left:178px;display:flex;gap:10px}
.social span{width:24px;height:24px;border-radius:50%;background:var(--purple)}
.social span:nth-child(2){background:var(--coral)}
.bottom{position:absolute;left:0;top:3527px;width:1200px;height:40px;background:var(--purple);color:#fff;font-size:11px;display:flex;align-items:center;justify-content:center}
</style>
</head>
<body>

<!-- HERO -->
<section class="hero" role="img" aria-label="Bearded yogi in orange robes meditating cross-legged on a mat in a warm sunlit room"></section>
<div class="logo" style="left:91px;top:16px">
  <span class="logo-dot"></span>
  <span class="logo-name">Quietfern<br>Meditation</span>
</div>
<nav class="nav">
  <span class="active">Home</span>
  <span>What Is Quietfern Meditation</span>
  <span>About Us</span>
  <span>Sessions</span>
  <span>Events</span>
  <span>Resources</span>
  <span>Contact Us</span>
  <span class="region">AU&nbsp;&nbsp;NZ</span>
</nav>
<div class="btn" style="left:1019px;top:24px;width:88px;height:31px">Donate</div>
<h1 class="hero-title" style="top:254px">
  <span class="l1">Transform Your Life Through</span>
  <span class="l2">Yoga <b>And</b> Meditation</span>
</h1>
<div class="btn" style="left:536px;top:368px;width:128px;height:30px">Contact Now</div>

<!-- ABOUT -->
<span class="mark" style="top:718px"></span>
<h2 class="heading abs" style="left:0;width:1200px;top:748px;font-size:37px">About Quietfern Meditation</h2>
<p class="intro">Quietfern Meditation Is A Simple, Natural Meditation Technique Taught Freely To Help People Experience Inner Peace, Clarity, And Emotional Balance.</p>

<div class="feature" style="left:181px;top:868px">
  <svg width="36" height="36" viewBox="0 0 36 36" fill="none" stroke="#e9867c" stroke-width="1.6"><path d="M18 8c4 5 4 12 0 18-4-6-4-13 0-18z"/><path d="M10 14c5 1 8 6 8 12-6-1-9-6-8-12zM26 14c-5 1-8 6-8 12 6-1 9-6 8-12z"/><path d="M6 27h24" stroke="#a784c8"/></svg>
  Free Meditation<br>Sessions
</div>
<div class="feature" style="left:387px;top:868px">
  <svg width="36" height="36" viewBox="0 0 36 36" fill="none" stroke="#e9867c" stroke-width="1.6"><circle cx="18" cy="18" r="6" stroke="#a784c8"/><circle cx="18" cy="5" r="2.5"/><circle cx="18" cy="31" r="2.5"/><circle cx="5" cy="18" r="2.5"/><circle cx="31" cy="18" r="2.5"/><circle cx="9" cy="9" r="2.5"/><circle cx="27" cy="9" r="2.5"/><circle cx="9" cy="27" r="2.5"/><circle cx="27" cy="27" r="2.5"/></svg>
  Community<br>Programs
</div>
<div class="feature" style="left:581px;top:868px">
  <svg width="36" height="36" viewBox="0 0 36 36" fill="none" stroke="#e9867c" stroke-width="1.6"><rect x="4" y="7" width="28" height="25" rx="2"/><path d="M4 13h28M11 4v6M25 4v6"/><path d="M13 23l4 3 7-7" stroke="#a784c8"/></svg>
  Tavolin<br>Events
</div>
<div class="feature" style="left:792px;top:868px">
  <svg width="36" height="36" viewBox="0 0 36 36" fill="none" stroke="#e9867c" stroke-width="1.6"><path d="M4 26c5-3 9-3 13-1h7c2 0 2 3 0 3h-7"/><path d="M4 30c6-2 12 1 18 0l10-6c2-1 0-4-2-3l-6 3"/><path d="M25 6c2-2 6 0 4 4l-5 5-5-5c-2-4 2-6 4-4l1 1z" stroke="#a784c8"/></svg>
  Donation Drives For Building<br>A Meditation Centre
</div>

<!-- ORGANISATION -->
<div class="photo" role="img" aria-label="Award ceremony with a spiritual teacher in white receiving a framed certificate on a stage" style="left:201px;top:1039px;width:386px;height:269px;background:linear-gradient(135deg,#2c3e8c,#4a5aa6 45%,#d8c6b9 70%,#7a3b2e)"></div>
<div class="photo" role="img" aria-label="Group of people seated on red carpets at a meditation gathering" style="left:156px;top:1209px;width:230px;height:162px;background:linear-gradient(135deg,#6b4a43,#a23a34 60%,#c84b46);border:3px solid #fff"></div>
<span class="mark" style="left:660px;top:1066px"></span>
<h2 class="heading abs" style="left:656px;top:1098px;font-size:37px;text-align:left">About The Organisation</h2>
<p class="org-text" style="top:1151px">Welcome, Seeker Of Wisdom And Tranquility! Ready To Sprinkle A Pinch Of Zen In Your Life? Let's Unwrap The Joyous Gift That Is Tavolin Meditation Together.</p>
<p class="org-text" style="top:1218px">Tavolin Meditation Is Like Your Favourite Playlist For The Soul, A Harmonious Blend Of Spiritual Awakening, Physical Wellness, And Mental Peace. Rooted In The Profound Teachings Of His Holiness Swami Anandavel, This Practice Is A Universal Passport To Inner Peace, Open To Everyone, Regardless Of Race, Religion, Or How You Like Your Coffee!</p>
<div class="btn" style="left:656px;top:1329px;width:111px;height:31px">Read More</div>
<div class="btn" style="left:780px;top:1329px;width:88px;height:31px">Donate</div>

<!-- SESSIONS -->
<section class="sessions">
  <span class="mark" style="top:76px"></span>
  <h2 class="heading abs" style="left:0;width:1200px;top:104px;font-size:37px">Sessions</h2>

  <div class="card" style="left:156px">
    <div class="img" role="img" aria-label="Woman in a grey blazer in a meditative hand gesture beside green plants" style="background:linear-gradient(135deg,#2f3a2a,#7d8a8d 55%,#3b5a2e)"></div>
    <h3>Fernvale Ridge - VIC<br>Meditation Centre</h3>
    <div class="row"><svg width="9" height="11" viewBox="0 0 9 11"><path d="M4.5 0a4 4 0 0 1 4 4c0 3-4 7-4 7S.5 7 .5 4a4 4 0 0 1 4-4z" fill="#a784c8"/></svg>12 Larkmoor St, Fernvale<br>Ridge VIC 3990, Australia</div>
    <div class="row"><svg width="10" height="10" viewBox="0 0 10 10" fill="none" stroke="#a784c8"><circle cx="5" cy="5" r="4.2"/><path d="M5 2.5V5l2 1"/></svg>Every Thursday 6:45 - 7:15 PM</div>
    <div class="row" style="margin-top:10px"><svg width="10" height="10" viewBox="0 0 10 10"><path d="M2 0l2 2.5-1.2 1.3a6 6 0 0 0 3.4 3.4L7.5 6 10 8 8.5 10C4 10 0 6 0 1.5z" fill="#a784c8"/></svg>Anika&nbsp;&nbsp;<u>+61 400 111 201</u></div>
  </div>

  <div class="card" style="left:385px">
    <div class="img" role="img" aria-label="Woman in black meditating cross-legged on a mat in a park" style="background:linear-gradient(180deg,#5c7a3e,#8ea35a 55%,#6b5e86)"></div>
    <h3>Willowmere - VIC<br>Meditation Centre</h3>
    <div class="row"><svg width="9" height="11" viewBox="0 0 9 11"><path d="M4.5 0a4 4 0 0 1 4 4c0 3-4 7-4 7S.5 7 .5 4a4 4 0 0 1 4-4z" fill="#a784c8"/></svg>24 Orrin Blvd, Willowmere<br>VIC 3342, Australia</div>
    <div class="row"><svg width="10" height="10" viewBox="0 0 10 10" fill="none" stroke="#a784c8"><circle cx="5" cy="5" r="4.2"/><path d="M5 2.5V5l2 1"/></svg>Every Monday 6:30 - 7:00 PM</div>
    <div class="row" style="margin-top:10px"><svg width="10" height="10" viewBox="0 0 10 10"><path d="M2 0l2 2.5-1.2 1.3a6 6 0 0 0 3.4 3.4L7.5 6 10 8 8.5 10C4 10 0 6 0 1.5z" fill="#a784c8"/></svg>Mira&nbsp;&nbsp;<u>+61 400 111 202</u></div>
  </div>

  <div class="card" style="left:612px">
    <div class="img" role="img" aria-label="Two smiling women in grey tops standing side by side" style="background:linear-gradient(135deg,#e6e6e6,#9a9a9a 50%,#d8d8d8)"></div>
    <h3>Ashgrove - WA Meditation<br>Centre</h3>
    <div class="row"><svg width="9" height="11" viewBox="0 0 9 11"><path d="M4.5 0a4 4 0 0 1 4 4c0 3-4 7-4 7S.5 7 .5 4a4 4 0 0 1 4-4z" fill="#a784c8"/></svg>9B Calloway Crescent,<br>Ashgrove WA, Australia</div>
    <div class="row"><svg width="10" height="10" viewBox="0 0 10 10" fill="none" stroke="#a784c8"><circle cx="5" cy="5" r="4.2"/><path d="M5 2.5V5l2 1"/></svg>Every Sunday 6 AM</div>
    <div class="row" style="margin-top:10px;margin-bottom:2px"><svg width="10" height="10" viewBox="0 0 10 10"><path d="M2 0l2 2.5-1.2 1.3a6 6 0 0 0 3.4 3.4L7.5 6 10 8 8.5 10C4 10 0 6 0 1.5z" fill="#a784c8"/></svg>Riya&nbsp;&nbsp;<u>+61 400 111 203</u></div>
    <div class="row"><svg width="10" height="10" viewBox="0 0 10 10"><path d="M2 0l2 2.5-1.2 1.3a6 6 0 0 0 3.4 3.4L7.5 6 10 8 8.5 10C4 10 0 6 0 1.5z" fill="#a784c8"/></svg>Tara&nbsp;&nbsp;<u>+61 400 111 204</u></div>
  </div>

  <div class="card" style="left:840px">
    <div class="img" role="img" aria-label="Two women in sportswear with palms pressed together in a gym" style="background:linear-gradient(135deg,#d9d4cf,#8a7d78 50%,#c9a0a8)"></div>
    <h3>Shantivan (Main<br>Centre)</h3>
    <div class="row"><svg width="9" height="11" viewBox="0 0 9 11"><path d="M4.5 0a4 4 0 0 1 4 4c0 3-4 7-4 7S.5 7 .5 4a4 4 0 0 1 4-4z" fill="#a784c8"/></svg>Brightmoss, 270 Hollin Rd, Emberly<br>Creek VIC 3358, Australia</div>
    <div class="row"><svg width="10" height="10" viewBox="0 0 10 10" fill="none" stroke="#a784c8"><circle cx="5" cy="5" r="4.2"/><path d="M5 2.5V5l2 1"/></svg>Daily 8 AM To 8 PM</div>
    <div class="row" style="margin-top:10px;margin-bottom:2px"><svg width="10" height="10" viewBox="0 0 10 10"><path d="M2 0l2 2.5-1.2 1.3a6 6 0 0 0 3.4 3.4L7.5 6 10 8 8.5 10C4 10 0 6 0 1.5z" fill="#a784c8"/></svg>Lena Marwick&nbsp;&nbsp;<u>+61 400 111 205</u></div>
    <div class="row"><svg width="10" height="10" viewBox="0 0 10 10"><path d="M2 0l2 2.5-1.2 1.3a6 6 0 0 0 3.4 3.4L7.5 6 10 8 8.5 10C4 10 0 6 0 1.5z" fill="#a784c8"/></svg>Isha Korran&nbsp;&nbsp;<u>+61 400 111 206</u></div>
  </div>

  <div class="round" style="left:515px;top:503px"><svg width="12" height="12" viewBox="0 0 12 12" fill="none" stroke="#fff" stroke-width="1.6"><path d="M11 6H1M5 2L1 6l4 4"/></svg></div>
  <div class="btn" style="left:553px;top:503px;width:94px;height:31px">View All</div>
  <div class="round" style="left:654px;top:503px"><svg width="12" height="12" viewBox="0 0 12 12" fill="none" stroke="#fff" stroke-width="1.6"><path d="M1 6h10M7 2l4 4-4 4"/></svg></div>
</section>

<!-- EVENTS -->
<span class="mark" style="top:2137px"></span>
<h2 class="heading abs" style="left:0;width:1200px;top:2164px;font-size:37px">Events &amp; Programs</h2>

<div class="photo" role="img" aria-label="Smiling man taking a selfie with a group of meditation participants indoors" style="left:156px;top:2239px;width:225px;height:275px;background:linear-gradient(160deg,#8b7a64,#5e574f 50%,#2f2b28)"></div>
<div class="abs" style="left:406px;top:2276px;width:160px">
  <div class="ev-title">Lorem Ipsum Is Simply Dummy Text Of The Printing Industry.</div>
  <div class="ev-meta" style="margin-top:22px"><svg width="10" height="10" viewBox="0 0 10 10" fill="none" stroke="#a784c8"><rect x=".5" y="1.5" width="9" height="8"/><path d="M.5 4h9"/></svg>Jan 18, 2026</div>
  <div class="ev-meta"><svg width="10" height="10" viewBox="0 0 10 10" fill="none" stroke="#a784c8"><circle cx="5" cy="5" r="4.2"/><path d="M5 2.5V5l2 1"/></svg>3:30 Pm - 5:00 Pm</div>
  <div class="ev-meta"><svg width="9" height="11" viewBox="0 0 9 11"><path d="M4.5 0a4 4 0 0 1 4 4c0 3-4 7-4 7S.5 7 .5 4a4 4 0 0 1 4-4z" fill="#a784c8"/></svg>Lorem Ipsum 3336, Australia</div>
</div>
<div class="btn" style="left:406px;top:2448px;width:109px;height:30px">Book Now</div>

<div class="divider" style="left:612px;top:2229px;width:432px"></div>
<div class="photo" role="img" aria-label="Young woman in a floral top holding flowers in a doorway" style="left:613px;top:2239px;width:125px;height:125px;background:linear-gradient(135deg,#c9a45a,#e2c6c6 50%,#8a6d5d)"></div>
<div class="abs" style="left:762px;top:2250px;width:250px">
  <div class="ev-title">Lorem Ipsum Is Simply Dummy<br>Text Of The Printing Industry.</div>
  <div class="ev-meta"><svg width="10" height="10" viewBox="0 0 10 10" fill="none" stroke="#a784c8"><rect x=".5" y="1.5" width="9" height="8"/><path d="M.5 4h9"/></svg>Jan 18, 2026<span style="width:55px"></span><svg width="10" height="10" viewBox="0 0 10 10" fill="none" stroke="#a784c8"><circle cx="5" cy="5" r="4.2"/><path d="M5 2.5V5l2 1"/></svg>3:30 Pm - 5:00 Pm</div>
  <div class="ev-meta"><svg width="9" height="11" viewBox="0 0 9 11"><path d="M4.5 0a4 4 0 0 1 4 4c0 3-4 7-4 7S.5 7 .5 4a4 4 0 0 1 4-4z" fill="#a784c8"/></svg>Lorem Ipsum 3336, Australia</div>
  <div style="font-size:10px;text-decoration:underline;margin-top:18px">Book Now</div>
</div>
<div class="divider" style="left:612px;top:2377px;width:432px"></div>
<div class="photo" role="img" aria-label="Two people meditating with palms together outdoors in a field" style="left:613px;top:2390px;width:125px;height:125px;background:linear-gradient(135deg,#a8b8c6,#c98a5a 50%,#6b7a4a)"></div>
<div class="abs" style="left:762px;top:2401px;width:250px">
  <div class="ev-title">Lorem Ipsum Is Simply Dummy<br>Text Of The Printing Industry.</div>
  <div class="ev-meta"><svg width="10" height="10" viewBox="0 0 10 10" fill="none" stroke="#a784c8"><rect x=".5" y="1.5" width="9" height="8"/><path d="M.5 4h9"/></svg>Jan 18, 2026<span style="width:55px"></span><svg width="10" height="10" viewBox="0 0 10 10" fill="none" stroke="#a784c8"><circle cx="5" cy="5" r="4.2"/><path d="M5 2.5V5l2 1"/></svg>3:30 Pm - 5:00 Pm</div>
  <div class="ev-meta"><svg width="9" height="11" viewBox="0 0 9 11"><path d="M4.5 0a4 4 0 0 1 4 4c0 3-4 7-4 7S.5 7 .5 4a4 4 0 0 1 4-4z" fill="#a784c8"/></svg>Lorem Ipsum 3336, Australia</div>
  <div style="font-size:10px;text-decoration:underline;margin-top:18px">Book Now</div>
</div>
<div class="divider" style="left:612px;top:2527px;width:432px"></div>

<div class="btn" style="left:502px;top:2558px;width:95px;height:31px">View All</div>
<div class="btn" style="left:609px;top:2558px;width:88px;height:31px">Donate</div>

<!-- RESOURCES -->
<section class="resources">
  <span class="mark" style="top:78px"></span>
  <h2 class="heading abs" style="left:0;width:1200px;top:106px;font-size:37px">Resources</h2>

  <div class="photo" role="img" aria-label="Woman meditating cross-legged on the floor in a bright studio with a group" style="left:156px;top:168px;width:431px;height:279px;background:linear-gradient(135deg,#5a3f2e,#c8b7a6 45%,#6f8aa8 60%,#3a2f2a)"><span class="tag">Video</span></div>
  <div class="photo" role="img" aria-label="Man with palms pressed together leading a large outdoor meditation group at sunset" style="left:613px;top:168px;width:431px;height:279px;background:linear-gradient(135deg,#e0a85a,#8a6a4a 45%,#3a3a42 75%,#6a5a4a)"><span class="tag">Articles</span></div>

  <div class="res-cap" style="left:202px;top:464px">
    <svg width="26" height="26" viewBox="0 0 26 26"><circle cx="13" cy="13" r="13" fill="#a784c8"/><path d="M10 8l8 5-8 5z" fill="#fff"/></svg>
    <span>Lorem Ipsum Is Simply Dummy Text Of The<br>Printing Industry.</span>
  </div>
  <div class="res-cap" style="left:660px;top:464px">
    <svg width="24" height="26" viewBox="0 0 24 26"><rect x="4" y="1" width="18" height="24" rx="2" fill="#f3a89f"/><rect x="0" y="8" width="8" height="17" rx="2" fill="#e9867c"/><path d="M9 7h9M9 11h9M9 15h9" stroke="#fff" stroke-width="1.4"/></svg>
    <span>Lorem Ipsum Is Simply Dummy Text Of The<br>Printing Industry.</span>
  </div>

  <div class="round" style="left:515px;top:523px"><svg width="12" height="12" viewBox="0 0 12 12" fill="none" stroke="#fff" stroke-width="1.6"><path d="M11 6H1M5 2L1 6l4 4"/></svg></div>
  <div class="btn" style="left:553px;top:523px;width:94px;height:31px">View All</div>
  <div class="round" style="left:654px;top:523px"><svg width="12" height="12" viewBox="0 0 12 12" fill="none" stroke="#fff" stroke-width="1.6"><path d="M1 6h10M7 2l4 4-4 4"/></svg></div>
</section>

<!-- FOOTER -->
<footer class="footer">
  <div class="logo" style="left:158px;top:52px">
    <span class="logo-dot" style="width:50px;height:50px"></span>
    <span class="logo-name" style="font-size:17px">Quietfern<br>Meditation</span>
  </div>
  <div class="social"><span></span><span></span><span></span><span></span></div>

  <div class="fcol" style="left:382px">
    <h4>CONTACT US</h4>
    <div style="display:flex;gap:6px;align-items:center;margin-bottom:6px"><svg width="10" height="10" viewBox="0 0 10 10"><path d="M2 0l2 2.5-1.2 1.3a6 6 0 0 0 3.4 3.4L7.5 6 10 8 8.5 10C4 10 0 6 0 1.5z" fill="#a784c8"/></svg>+1300 000 418</div>
    <div style="display:flex;gap:6px;align-items:center;margin-bottom:6px"><svg width="11" height="8" viewBox="0 0 11 8"><rect width="11" height="8" fill="#a784c8"/><path d="M0 0l5.5 4L11 0" stroke="#1b1515" fill="none"/></svg>hello@quietfernmeditation.org.au</div>
    <div style="display:flex;gap:6px"><svg width="9" height="11" viewBox="0 0 9 11" style="margin-top:3px"><path d="M4.5 0a4 4 0 0 1 4 4c0 3-4 7-4 7S.5 7 .5 4a4 4 0 0 1 4-4z" fill="#a784c8"/></svg><span>270 Hollin Road, Emberly Creek,<br>Victoria, 3358</span></div>
  </div>

  <div class="fcol" style="left:630px;line-height:1.6">
    <h4>QUICK LINKS</h4>
    <div style="color:var(--coral);text-decoration:underline">Home</div>
    <div>What Is Quietfern Meditation</div>
    <div>About Us</div>
    <div>Sessions</div>
    <div>Events</div>
    <div>Resources</div>
    <div>Contact Us</div>
  </div>

  <div class="photo" role="img" aria-label="Street map showing the meditation centre location with a red pin" style="left:837px;top:50px;width:207px;height:143px;background:linear-gradient(135deg,#e8efe9,#f4f4f0 50%,#dfe9e2);border-radius:3px"></div>
</footer>
<div class="bottom">© 2026 Tavolin Meditation Australia. All Right Reserved</div>

</body>
</html>
```